Stationary design for boutique production house

We need a stationary design for our production house, 'Luma Studios' based in Singapore. We produce microfilms as well as podcasts, talkshows and events. Our logo is a stylized icon of our director, who is also the executive producer and host of our programs, Orla. Our main company colors are Red, Black and white. We would like a clean, minimalist design incorporating our existing company logo that conveys a sense of urbanism and elegance.

Logo and font files are attached. f

Target Market(s)

We focus on lifestyle media rather than entertainment.

Industry/Entity Type

Boutique

Font styles to use
Serif
Sans Serif

Colors
ec1f27
ffffff
000000

Requirements
Must have
• Our company logo and at least one of our company colors.
Nice to have
• Our address and contact information.
Should not have
• Changes made to the company logo (using only certain parts of it is fine though)

```html
<!DOCTYPE html>
<html lang="en">
<head>
<meta charset="utf-8">
<title>Luma Studios — Stationery</title>
<link rel="stylesheet" href="https://fonts.googleapis.com/css2?family=Roboto:wght@400;500;700&display=swap">
<style>
  :root {
    --brand-red: #ec1f27;
    --ink: #333333;
    --paper: #ffffff;
    --stage: #ebebeb;
    --body-text: #555555;
    --sans: "Roboto", Arial, sans-serif;
  }
  * { box-sizing: border-box; margin: 0; padding: 0; }
  html, body { width: 1200px; height: 937px; overflow: hidden; background: var(--stage); }
  .stage { position: relative; width: 1200px; height: 937px; font-family: var(--sans); color: var(--ink); }
  .sheet { position: absolute; background: var(--paper); overflow: hidden; }
  .wave { position: absolute; left: 0; bottom: 0; width: 100%; display: block; }

  .brand-name { font-family: var(--sans); font-weight: 500; color: var(--ink); line-height: 1; letter-spacing: 0.08em; white-space: nowrap; }

  /* Letterhead */
  .letterhead { left: 185px; top: 68px; width: 387px; height: 544px; }
  .letterhead .brand-name { position: absolute; left: 24px; top: 112px; font-size: 30px; }
  .contact-list { position: absolute; right: 16px; top: 22px; list-style: none; text-align: right; font-size: 4.6px; line-height: 8px; color: var(--ink); }
  .contact-list li { display: flex; justify-content: flex-end; align-items: center; gap: 3px; }
  .contact-list li::after { content: ""; width: 5px; height: 5px; border-radius: 50%; background: var(--ink); }
  .letter { position: absolute; left: 36px; top: 192px; width: 300px; font-size: 5.3px; line-height: 8.2px; color: var(--body-text); }
  .letter p { margin-bottom: 8px; }
  .letter .salutation strong, .letter .sender strong { color: var(--ink); }
  .letter .signature { width: 40px; height: 22px; margin: 2px 0 6px; }

  /* Cover */
  .cover { left: 636px; top: 41px; width: 458px; height: 575px; }
  .cover .brand-name { position: absolute; left: 0; right: 0; top: 360px; text-align: center; font-size: 44px; }
  .web { position: absolute; font-family: var(--sans); color: var(--paper); letter-spacing: 0.22em; }
  .cover .web { right: 16px; bottom: 11px; font-size: 11.5px; }

  /* Business cards */
  .card { width: 176px; height: 100px; border-radius: 7px; left: 46px; }
  .card-front { top: 658px; }
  .card-front .brand-name { position: absolute; left: 16px; top: 16px; font-size: 14px; }
  .card-front .person { position: absolute; left: 16px; top: 52px; font-size: 5.4px; line-height: 6.4px; }
  .card-front .person strong { display: block; font-weight: 700; letter-spacing: 0.03em; }
  .card-front .contact-list { left: 102px; right: auto; top: 71px; text-align: left; color: var(--paper); font-size: 3.4px; line-height: 5.3px; }
  .card-front .contact-list li { justify-content: flex-start; flex-direction: row-reverse; }
  .card-front .contact-list li::after { width: 3.5px; height: 3.5px; background: var(--paper); }
  .card-back { top: 785px; }
  .card-back .brand-name { position: absolute; left: 0; right: 0; top: 41px; text-align: center; font-size: 17px; }

  /* Envelopes */
  .envelope-front { left: 265px; top: 672px; width: 438px; height: 208px; }
  .envelope-front .brand-name { position: absolute; left: 20px; top: 78px; font-size: 21px; }
  .envelope-front .web { right: 22px; bottom: 10px; font-size: 9.5px; }
  .envelope-back { left: 737px; top: 672px; width: 432px; height: 208px; }
  .envelope-flap { position: absolute; left: 0; top: 0; width: 100%; height: 72px; background: var(--ink); border-radius: 0 0 36px 36px; display: flex; align-items: center; justify-content: center; }
  .envelope-flap .web { position: static; font-size: 12px; }
</style>
</head>
<body>
<main class="stage">

  <section class="sheet letterhead" aria-label="Letterhead">
    <ul class="contact-list">
      <li>+65 6123 4501</li>
      <li>+65 6123 4502</li>
      <li>hello@lumastudios.sg</li>
      <li>www.lumastudios.sg</li>
      <li>12 Keong Saik Road, Singapore 089119</li>
    </ul>
    <div class="brand-name">ORLA</div>
    <article class="letter">
      <p class="date">July 2, 2012</p>
      <p class="salutation"><strong>Dear Mr. Lim,</strong><br>12 Keong Saik Road, Singapore</p>
      <p>Thank you for meeting with our team last week. We are pleased to share a proposal for the lifestyle series we discussed, covering concept, casting, location scouting and a full production schedule. Our crew will handle filming, sound and editing in house, with a first cut ready within six weeks of the shoot.</p>
      <p>Please find the budget breakdown attached. Every line is itemised so you can review each stage before we begin.</p>
      <p>We would welcome a short call to confirm dates, talent and the tone of the episodes. Once approved, we can reserve the studio and begin pre-production straight away, keeping you updated at every milestone until final delivery.</p>
      <p class="closing">Best Regards,</p>
      <svg class="signature" viewBox="0 0 40 22" aria-hidden="true"><path d="M3 18 C6 4 9 2 8 14 C10 8 14 6 13 15 C16 9 20 10 19 15 C23 11 27 12 26 15 L36 13" fill="none" stroke="#222" stroke-width="0.9"/></svg>
      <p class="sender"><strong>Daniel Ong</strong><br>Director<br>12 Keong Saik Road, Singapore</p>
    </article>
    <svg class="wave" viewBox="0 0 400 100" height="98" preserveAspectRatio="none" aria-hidden="true">
      <path d="M0 40 C120 98 260 12 400 0 L400 100 L0 100Z" fill="var(--brand-red)"/>
      <path d="M0 58 C130 104 270 28 400 18 L400 100 L0 100Z" fill="var(--paper)"/>
      <path d="M0 66 C130 108 270 38 400 28 L400 100 L0 100Z" fill="var(--ink)"/>
      <path d="M0 84 C140 112 280 54 400 46" fill="none" stroke="var(--paper)" stroke-width="1.4"/>
    </svg>
  </section>

  <section class="sheet cover" aria-label="Presentation cover">
    <div class="brand-name">ORLA</div>
    <svg class="wave" viewBox="0 0 400 100" height="112" preserveAspectRatio="none" aria-hidden="true">
      <path d="M0 30 C110 90 250 10 400 0 L400 100 L0 100Z" fill="var(--brand-red)"/>
      <path d="M0 50 C120 98 260 28 400 20 L400 100 L0 100Z" fill="var(--paper)"/>
      <path d="M0 58 C120 104 260 38 400 30 L400 100 L0 100Z" fill="var(--ink)"/>
      <path d="M0 78 C140 110 280 56 400 48" fill="none" stroke="var(--paper)" stroke-width="1.4"/>
    </svg>
    <span class="web">www.lumastudios.sg</span>
  </section>

  <section class="sheet card card-front" aria-label="Business card, front">
    <svg class="wave" viewBox="0 0 200 100" height="58" preserveAspectRatio="none" aria-hidden="true">
      <path d="M0 45 C60 95 130 10 200 0 L200 100 L0 100Z" fill="var(--brand-red)"/>
      <path d="M0 58 C70 100 140 22 200 16 L200 100 L0 100Z" fill="var(--paper)"/>
      <path d="M0 64 C70 104 140 32 200 26 L200 100 L0 100Z" fill="var(--ink)"/>
    </svg>
    <div class="brand-name">ORLA</div>
    <p class="person"><strong>MARCUS TAN</strong>Managing Director</p>
    <ul class="contact-list">
      <li>+65 6123 4501</li>
      <li>+65 6123 4502</li>
      <li>hello@lumastudios.sg</li>
      <li>www.lumastudios.sg</li>
      <li>12 Keong Saik Road, Singapore 089119</li>
    </ul>
  </section>

  <section class="sheet card card-back" aria-label="Business card, back">
    <div class="brand-name">ORLA</div>
  </section>

  <section class="sheet envelope-front" aria-label="Envelope, front">
    <div class="brand-name">ORLA</div>
    <svg class="wave" viewBox="0 0 400 100" height="118" preserveAspectRatio="none" aria-hidden="true">
      <path d="M0 42 C120 100 260 8 400 0 L400 100 L0 100Z" fill="var(--brand-red)"/>
      <path d="M0 60 C130 104 270 24 400 16 L400 100 L0 100Z" fill="var(--paper)"/>
      <path d="M0 68 C130 108 270 34 400 26 L400 100 L0 100Z" fill="var(--ink)"/>
      <path d="M0 86 C140 112 280 54 400 46" fill="none" stroke="var(--paper)" stroke-width="1.2"/>
    </svg>
    <span class="web">www.lumastudios.sg</span>
  </section>

  <section class="sheet envelope-back" aria-label="Envelope, back">
    <div class="envelope-flap"><span class="web">www.lumastudios.sg</span></div>
  </section>

</main>
</body>
</html>
```